Salve Label

2.25 inch round label.

We are looking for a simple label, muted natural colors, sophisticated, elegant, calming.

Name of Product: Herbal Beeswax Salve
This scent is lavender - but there will be others scents
Want this label to be adaptable to other scents with simple color and word changes.

Other things to express on the label - all natural, calming, relaxing

Name of the Company: Copper Hollow Farm
2 oz.

```html
<!DOCTYPE html>
<html lang="en">
<head>
<meta charset="utf-8">
<title>Copper Hollow Farm – Herbal Beeswax Salve Label</title>
<link rel="stylesheet" href="https://fonts.googleapis.com/css2?family=Fira+Sans:ital,wght@0,400;0,500;0,600;1,400&display=swap">
<style>
  :root {
    --page: #ffffff;
    --rim: #8e9779;
    --label: #eef0e3;
    --band: #a8ae8d;
    --pattern: #d4d8c3;
    --ink: #5a6838;
    --rule: #6c7652;
    --light: #ffffff;
  }
  html, body {
    margin: 0;
    padding: 0;
    width: 1003px;
    height: 1200px;
    overflow: hidden;
    background: var(--page);
  }
  .canvas {
    position: relative;
    width: 1003px;
    height: 1200px;
    font-family: "Fira Sans", sans-serif;
  }
  .label-shapes {
    position: absolute;
    inset: 0;
  }
  .text {
    position: absolute;
    left: 0;
    width: 1003px;
    text-align: center;
    margin: 0;
    line-height: 1;
  }
  .brand-name {
    top: 405px;
    font-size: 48px;
    font-weight: 500;
    color: var(--ink);
    letter-spacing: 1px;
  }
  .brand-dot {
    position: absolute;
    left: 473px;
    top: 300px;
    width: 56px;
    height: 56px;
    border-radius: 50%;
    background: var(--rim);
  }
  .product-name {
    top: 585px;
    font-size: 62px;
    font-style: italic;
    font-weight: 400;
    color: var(--light);
  }
  .benefits {
    top: 658px;
    font-size: 34px;
    font-weight: 400;
    color: var(--light);
  }
  .scent {
    top: 834px;
    font-size: 42px;
    font-weight: 600;
    letter-spacing: 7px;
    color: var(--ink);
  }
  .net-weight {
    top: 922px;
    font-size: 37px;
    font-weight: 400;
    color: var(--ink);
  }
</style>
</head>
<body>
<main class="canvas">
  <svg class="label-shapes" width="1003" height="1200" viewBox="0 0 1003 1200" xmlns="http://www.w3.org/2000/svg">
    <defs>
      <clipPath id="label-face">
        <circle cx="501" cy="600" r="420"/>
      </clipPath>
      <linearGradient id="pattern-fade" x1="0" y1="0" x2="1" y2="1">
        <stop offset="0" stop-color="var(--pattern)" stop-opacity="0.5"/>
        <stop offset="1" stop-color="var(--pattern)" stop-opacity="1"/>
      </linearGradient>
    </defs>
    <circle class="label-rim" cx="501" cy="600" r="450" fill="var(--rim)"/>
    <circle class="label-face" cx="501" cy="600" r="420" fill="var(--label)"/>
    <g clip-path="url(#label-face)">
      <path class="pattern-area" role="img" aria-label="Soft honeycomb pattern, upper left"
            d="M70 250 L300 235 L400 330 L400 524 L70 524 Z" fill="url(#pattern-fade)"/>
      <path class="pattern-area" role="img" aria-label="Soft honeycomb pattern, lower right"
            d="M670 762 L940 762 L940 1040 L720 1040 L660 900 Z" fill="url(#pattern-fade)"/>
      <rect class="title-band" x="0" y="524" width="1003" height="238" fill="var(--band)"/>
    </g>
    <circle class="inner-rule" cx="501" cy="600" r="405" fill="none" stroke="var(--rule)" stroke-width="2"/>
  </svg>

  <span class="brand-dot" aria-hidden="true"></span>
  <p class="text brand-name">Copper Hollow Farm</p>
  <h1 class="text product-name">Herbal Beeswax Salve</h1>
  <p class="text benefits">All natural, calming, relaxing</p>
  <p class="text scent">LAVENDER</p>
  <p class="text net-weight">Net wt. 2oz</p>
</main>
</body>
</html>
```